Business cards Dör Kornhüüs GmbH & Co.KG

We need a uniform business card design template for our employees.
A template should be created to have the same design for all business cards.

Contact Information for Business Card

Firma und Firmierung, Name, Funktion in Unternehmen, Anschrift, Tel. Handynummer, Emailadresse, Internetseite

Colors

Designer to choose colors to be used in the design.

Requirements
Must have
• Our company logo must be on it

```html
<!DOCTYPE html>
<html lang="de">
<head>
<meta charset="utf-8">
<title>Visitenkarte Dör Kornhüüs</title>
<link rel="stylesheet" href="https://fonts.googleapis.com/css2?family=Bebas+Neue&family=Open+Sans:wght@400;600&display=swap">
<style>
  :root {
    --page-bg: #e4e4e7;
    --card-bg: #ffffff;
    --brand-purple: #8e3794;
    --brand-lilac: #c99dc9;
    --brand-coral: #f0707f;
    --name-grey: #a48aa8;
    --text-dark: #333333;
  }
  html, body {
    margin: 0;
    padding: 0;
    width: 1200px;
    height: 1200px;
    overflow: hidden;
    background: var(--page-bg);
  }
  .card {
    position: absolute;
    left: 50px;
    top: 270px;
    width: 1100px;
    height: 659px;
    background: var(--card-bg);
    overflow: hidden;
    box-shadow: 0 6px 18px rgba(0,0,0,0.18);
  }
  .card-accent {
    position: absolute;
    inset: 0;
    width: 1100px;
    height: 659px;
  }
  .brand-mark {
    position: absolute;
    left: 110px;
    top: 140px;
    display: flex;
    align-items: center;
    gap: 14px;
  }
  .brand-dot {
    width: 24px;
    height: 24px;
    border-radius: 50%;
    background: var(--brand-lilac);
    flex: none;
  }
  .brand-name {
    margin: 0;
    font-family: "Open Sans", sans-serif;
    font-weight: 600;
    font-size: 50px;
    line-height: 1;
    color: var(--brand-coral);
  }
  .company-line {
    position: absolute;
    left: 114px;
    top: 243px;
    margin: 0;
    font-family: "Open Sans", sans-serif;
    font-size: 21px;
    color: var(--brand-purple);
  }
  .person-name {
    position: absolute;
    left: 112px;
    top: 315px;
    margin: 0;
    font-family: "Bebas Neue", sans-serif;
    font-weight: 400;
    font-size: 58px;
    line-height: 1;
    color: var(--name-grey);
  }
  .contact-list {
    position: absolute;
    left: 108px;
    top: 420px;
    margin: 0;
    padding: 0;
    list-style: none;
    font-family: "Open Sans", sans-serif;
    font-size: 26px;
    color: var(--text-dark);
  }
  .contact-item {
    display: flex;
    align-items: center;
    height: 44px;
  }
  .contact-icon {
    width: 22px;
    height: 22px;
    margin-right: 18px;
    fill: var(--brand-purple);
    flex: none;
  }
</style>
</head>
<body>
  <div class="card">
    <svg class="card-accent" viewBox="0 0 1100 659" role="img" aria-label="Geschwungene Farbfläche in Flieder, Koralle und Violett">
      <defs>
        <linearGradient id="accent-fill" x1="0" y1="0" x2="1" y2="0">
          <stop offset="0" stop-color="var(--brand-lilac)"/>
          <stop offset="0.45" stop-color="var(--brand-coral)"/>
          <stop offset="1" stop-color="var(--brand-purple)"/>
        </linearGradient>
      </defs>
      <path fill="url(#accent-fill)" d="M640 0 L1100 0 L1100 659 L610 659 C780 610 880 500 900 340 C915 200 820 80 640 0 Z"/>
    </svg>

    <div class="brand-mark">
      <span class="brand-dot"></span>
      <p class="brand-name">Dör Kornhüüs</p>
    </div>

    <p class="company-line">Visitenkarten Dör Kornhüüs GmbH &amp; Co.KG</p>
    <h1 class="person-name">Hanne Feldmann</h1>

    <ul class="contact-list">
      <li class="contact-item">
        <svg class="contact-icon" viewBox="0 0 24 24"><path d="M12 1C7.6 1 4.5 4.3 4.5 8.5 4.5 14 12 23 12 23s7.5-9 7.5-14.5C19.5 4.3 16.4 1 12 1z"/></svg>
        <span>doer-kornhuues.de</span>
      </li>
      <li class="contact-item">
        <svg class="contact-icon" viewBox="0 0 24 24"><path d="M6.6 10.8c1.4 2.8 3.8 5.1 6.6 6.6l2.2-2.2c.3-.3.7-.4 1-.2 1.1.4 2.3.6 3.6.6.6 0 1 .4 1 1V20c0 .6-.4 1-1 1C10.6 21 3 13.4 3 4c0-.6.4-1 1-1h3.5c.6 0 1 .4 1 1 0 1.3.2 2.5.6 3.6.1.3 0 .7-.2 1l-2.3 2.2z"/></svg>
        <span>0401552764</span>
      </li>
      <li class="contact-item">
        <svg class="contact-icon" viewBox="0 0 24 24"><path d="M2 5h20v14H2z M3.5 6.5l8.5 6.5 8.5-6.5" stroke="#fff" stroke-width="1.4"/></svg>
        <span>info@doer-kornhuues.de</span>
      </li>
      <li class="contact-item">
        <svg class="contact-icon" viewBox="0 0 24 24"><circle cx="12" cy="12" r="10" fill="none" stroke="var(--brand-purple)" stroke-width="2"/><path d="M2 12h20M12 2c3 3 3 17 0 20M12 2c-3 3-3 17 0 20M4 7h16M4 17h16" fill="none" stroke="var(--brand-purple)" stroke-width="1.6"/></svg>
        <span>doer-kornhuues.de</span>
      </li>
    </ul>
  </div>
</body>
</html>
```